Letterhead Design Project

Standard A4 paper, center the name Brightway Wash (with the mop) same as front of business card.
47 Harbour Vale Rd Kelston 5062 ABN: 71205839416
M. 0427163958 T. 83917605 Calibri font

Industry/Entity Type

Business

```html
<!DOCTYPE html>
<html lang="en">
<head>
<meta charset="utf-8">
<title>Brightway Wash Letterhead</title>
<link href="https://fonts.googleapis.com/css2?family=Carlito:wght@400;700&display=swap" rel="stylesheet">
<style>
  :root {
    --brand-navy: #1a2db8;
    --brand-sky: #6495f5;
    --paper: #ffffff;
    --ink-light: #ffffff;
    --mark-faint: #e4e4e4;
  }
  html, body {
    margin: 0;
    padding: 0;
    width: 900px;
    height: 1200px;
    overflow: hidden;
    background: var(--paper);
  }
  .letterhead {
    position: relative;
    width: 900px;
    height: 1200px;
    background: var(--paper);
    font-family: "Carlito", "Calibri", sans-serif;
    overflow: hidden;
  }
  .letterhead__waves {
    position: absolute;
    inset: 0;
    width: 900px;
    height: 1200px;
  }
  .wave--navy { fill: var(--brand-navy); }
  .wave--sky { fill: var(--brand-sky); }
  .brand {
    position: absolute;
    left: 0;
    right: 0;
    top: 218px;
    display: flex;
    justify-content: center;
    align-items: center;
    gap: 14px;
  }
  .brand__name {
    margin: 0;
    font-size: 48px;
    font-weight: 700;
    line-height: 1;
    color: var(--brand-navy);
    letter-spacing: 0.5px;
  }
  .brand__mark {
    width: 34px;
    height: 34px;
    border-radius: 50%;
    background: var(--brand-navy);
    flex: none;
  }
  .footer-mark {
    position: absolute;
    right: 70px;
    top: 880px;
    width: 90px;
    height: 90px;
    border-radius: 50%;
    background: var(--mark-faint);
  }
  .contact-block {
    position: absolute;
    left: 48px;
    top: 1072px;
    margin: 0;
    color: var(--ink-light);
    font-size: 19px;
    line-height: 1.45;
    font-style: normal;
  }
  .contact-block__line { display: block; }
  .contact-block__tel { margin-left: 26px; }
</style>
</head>
<body>
  <main class="letterhead">
    <svg class="letterhead__waves" viewBox="0 0 900 1200" aria-hidden="true">
      <path class="wave--sky" d="M0,140 C250,120 440,50 560,0 H620 C470,90 260,175 0,205 Z"/>
      <path class="wave--navy" d="M0,0 H560 C440,50 250,120 0,150 Z"/>
      <path class="wave--sky" d="M0,1010 C200,960 450,1015 620,1035 C740,1050 840,1040 900,1012 V1200 H0 Z"/>
      <path class="wave--navy" d="M0,1048 C200,1000 450,1050 620,1062 C760,1072 850,1060 900,1042 V1200 H0 Z"/>
    </svg>

    <header class="brand">
      <h1 class="brand__name">Brightway Wash</h1>
      <span class="brand__mark" role="img" aria-label="Brand mark"></span>
    </header>

    <span class="footer-mark" role="img" aria-label="Faint brand mark"></span>

    <address class="contact-block">
      <span class="contact-block__line">47 Harbour Vale Rd Kelston 5062</span>
      <span class="contact-block__line">Mobile: 0427163958<span class="contact-block__tel">Tel: 83917605</span></span>
      <span class="contact-block__line">ABN: 71205839416</span>
    </address>
  </main>
</body>
</html>
```